MERROWGATE WINE LABEL RANGE PROJECT

We need an elegant wine label design for our new range of wine. We need 3 labels for the range

2015 Merrowgate Shiraz
2015 Merrowgate Cabernet
2015 Merrowgate Shiraz Cabernet

The Size is nominated at 120mm High x 70mm Wide (Front and Back) but we are open to creative expression even if size differs

We are open to any style of label and designer can work on their strengths. it can be modern/classic/old fashion etc

I will attach the tasting notes which shows the title of wine for front label and tasting notes and details to be included at back. Please leave space for a barcode.

Thanks
Tamir.

Target Market(s)

WINE DRINKERS 35-65

Requirements
Must have
• ELEGANCE

```html
<!DOCTYPE html>
<html lang="en">
<head>
<meta charset="utf-8">
<title>Merrowgate 2015 Shiraz Cabernet – Front Label</title>
<link rel="stylesheet" href="https://fonts.googleapis.com/css2?family=Great+Vibes&family=Playfair+Display+SC:wght@400&family=Playfair+Display:ital@1&display=swap">
<style>
  :root {
    --backdrop: #fbdccd;
    --label-black: #0e0b0b;
    --border-maroon: #6a111a;
    --gold: #d8ad55;
    --gold-soft: #c99a45;
    --wine-red: #cf2440;
    --grape-deep: #4a0c1c;
    --grape-light: #b0283d;
    --leaf: #4d7a2c;
    --volume-grey: #d9d2cc;
  }
  html, body {
    margin: 0;
    padding: 0;
    width: 960px;
    height: 1200px;
    overflow: hidden;
    background: var(--backdrop);
  }
  .canvas {
    position: relative;
    width: 960px;
    height: 1200px;
    background: var(--backdrop);
  }
  .front-label {
    position: absolute;
    left: 260px;
    top: 210px;
    width: 440px;
    height: 780px;
    filter: drop-shadow(0 14px 24px rgba(80, 30, 20, 0.18));
  }
  .label-shape-outer { fill: var(--border-maroon); stroke: var(--gold-soft); stroke-width: 1.5; }
  .label-shape-inner { fill: var(--label-black); stroke: var(--gold); stroke-width: 2.2; }
  .vintage {
    font-family: "Playfair Display", Georgia, serif;
    font-style: italic;
    font-size: 26px;
    fill: var(--gold);
  }
  .brand-name {
    font-family: "Great Vibes", cursive;
    font-size: 56px;
    fill: var(--gold);
  }
  .variety {
    font-family: "Playfair Display SC", Georgia, serif;
    font-size: 31px;
    letter-spacing: 1px;
    fill: var(--wine-red);
  }
  .volume {
    font-family: "Playfair Display SC", Georgia, serif;
    font-size: 19px;
    letter-spacing: 1px;
    fill: var(--volume-grey);
  }
</style>
</head>
<body>
<main class="canvas">
  <svg class="front-label" viewBox="0 0 440 780" xmlns="http://www.w3.org/2000/svg">
    <defs>
      <radialGradient id="grape-tone" cx="45%" cy="40%" r="60%">
        <stop offset="0%" stop-color="var(--grape-light)"/>
        <stop offset="100%" stop-color="var(--grape-deep)"/>
      </radialGradient>
      <path id="label-outline" d="M0,80 A50 50 0 0 0 50,30 L150,30 Q200,30 220,0 Q240,30 290,30 L390,30 A50 50 0 0 0 440,80 L440,700 A50 50 0 0 0 390,750 L290,750 Q240,750 220,780 Q200,750 150,750 L50,750 A50 50 0 0 0 0,700 Z"/>
    </defs>

    <use href="#label-outline" class="label-shape-outer"/>
    <use href="#label-outline" class="label-shape-inner" transform="translate(14 16) scale(0.9364 0.959)"/>

    <rect class="crest-ornament" x="180" y="48" width="80" height="16" rx="8" fill="var(--border-maroon)" role="img" aria-label="Small maroon flourish ornament at the crest of the label"/>

    <text class="vintage" x="220" y="128" text-anchor="middle">2015</text>
    <text class="brand-name" x="220" y="190" text-anchor="middle">Merrowgate</text>

    <ellipse class="fruit-illustration" cx="220" cy="300" rx="58" ry="48" fill="url(#grape-tone)" role="img" aria-label="Illustration of two dark red plums on a stem with a green leaf"/>

    <text class="variety" x="220" y="478" text-anchor="middle">Shiraz Cabernet</text>
    <text class="volume" x="220" y="545" text-anchor="middle">750ml</text>
  </svg>
</main>
</body>
</html>
```